Business Card for Wellness Clinic

We need a business card for our new logo. I want it to match the feel of the logo

Target Market(s)

Young professional families looking for holistic health care

Industry/Entity Type

Health And Wellness

Contact Information for Business Card

Our business Name: Brackenfield Health & wellness Centre, our phone #, email address...see attached old business card

Font styles to use
Sans Serif

Colors
33b8a4
cee9f5

Requirements
Must have
• my logo and business name
• Font is "Helvetica Neue LT Std 45 Light" and
• Only for "&" using font "Trajan pro bold"
• Use colors in the logo

```html
<!DOCTYPE html>
<html lang="en">
<head>
<meta charset="utf-8">
<title>Brackenfield Health &amp; Wellness Centre – Business Card</title>
<link rel="stylesheet" href="https://fonts.googleapis.com/css2?family=Crimson+Text&family=Roboto:wght@300&display=swap">
<style>
  :root {
    --teal: #33b8a4;
    --mint: #d7ece8;
    --paper: #ffffff;
    --ink: #1f1f1f;
    --backdrop: #4d4e50;
  }
  * { margin: 0; padding: 0; box-sizing: border-box; }
  html, body { width: 1200px; height: 437px; overflow: hidden; }
  body { background: var(--backdrop); position: relative; }

  .card {
    position: absolute;
    top: 74px;
    width: 509px;
    height: 290px;
    background: var(--paper);
    overflow: hidden;
  }
  .card--front { left: 79px; }
  .card--back { left: 614px; }

  .brand {
    position: absolute;
    left: 0; right: 0; top: 32px;
    text-align: center;
    font-family: "Roboto", sans-serif;
    font-weight: 300;
    color: var(--teal);
    z-index: 2;
  }
  .brand__mark {
    width: 44px; height: 44px;
    margin: 0 auto 22px;
    background: var(--teal);
    border-radius: 6px;
  }
  .brand__name { font-size: 21px; letter-spacing: 4px; line-height: 1; text-transform: uppercase; }
  .brand__sub { font-size: 12px; letter-spacing: 8px; margin-top: 8px; text-transform: uppercase; }

  .contact-band { position: absolute; left: 0; top: 180px; width: 509px; height: 52px; }
  .contact-band__person {
    position: absolute; left: 15px; top: 184px;
    font-family: "Crimson Text", serif; font-size: 17px; line-height: 21px; color: var(--paper);
  }
  .contact-band__phone {
    position: absolute; left: 340px; top: 195px;
    font-family: "Crimson Text", serif; font-size: 21px; color: var(--paper);
  }
  .address {
    position: absolute; left: 0; right: 0; top: 243px;
    text-align: center;
    font-family: "Crimson Text", serif; font-size: 13px; line-height: 19px; color: var(--ink);
  }

  .corner-shape {
    position: absolute; left: 357px; top: 108px;
    width: 190px; height: 220px;
    background: var(--mint);
    border-radius: 18px;
    z-index: 1;
  }
  .appointment {
    position: absolute; left: 105px; top: 180px;
    font-family: "Crimson Text", serif; font-size: 14px; line-height: 21px; color: var(--ink);
    z-index: 2;
  }
  .appointment__row { display: flex; align-items: baseline; }
  .appointment__line { display: inline-block; border-bottom: 1px solid var(--ink); height: 13px; margin-left: 2px; }
  .policy {
    position: absolute; left: 0; right: 0; top: 242px;
    text-align: center;
    font-family: "Crimson Text", serif; font-size: 14px; line-height: 19px; color: var(--ink);
    z-index: 2;
  }
</style>
</head>
<body>
  <section class="card card--front">
    <div class="brand">
      <div class="brand__mark"></div>
      <div class="brand__name">Brackenfield Health</div>
      <div class="brand__sub">&amp; Wellness Centre</div>
    </div>
    <svg class="contact-band" viewBox="0 0 509 52" aria-hidden="true">
      <rect width="509" height="52" fill="var(--teal)"/>
      <polygon points="265,0 280,0 264,52 249,52" fill="var(--paper)"/>
    </svg>
    <div class="contact-band__person">Dr. Marianne Holt, N.D.<br>Naturopathic Doctor</div>
    <div class="contact-band__phone">613 555 0142</div>
    <div class="address">
      48 Alder Row W, Suite 210, Ottawa, ON K2P 0Z1<br>
      www.brackenfieldnaturopathic.ca | mholt@brackenfieldnaturopathic.ca
    </div>
  </section>

  <section class="card card--back">
    <div class="corner-shape"></div>
    <div class="brand">
      <div class="brand__mark"></div>
      <div class="brand__name">Brackenfield Health</div>
      <div class="brand__sub">&amp; Wellness Centre</div>
    </div>
    <div class="appointment">
      <div class="appointment__row">Date: <span class="appointment__line" style="width:118px"></span>Time:<span class="appointment__line" style="width:108px"></span></div>
      <div class="appointment__row">For: <span class="appointment__line" style="width:268px"></span></div>
    </div>
    <div class="policy">
      If you are unable to keep your appointment, please provide<br>
      at least 2 business days notice or full visit fees will apply.
    </div>
  </section>
</body>
</html>
```